Quolvex custom business card design

Need a authentic, innovative business card design for a new mobile app business. I am uploading a few screen images from our app for you to view. I would like app design theme to match business card design. I can also send logo images.

```html
<!DOCTYPE html>
<html lang="en">
<head>
<meta charset="utf-8">
<title>Quolvex business card</title>
<link href="https://fonts.googleapis.com/css2?family=Open+Sans:wght@400;600;800&display=swap" rel="stylesheet">
<style>
  :root {
    --stage: #3a3b3d;
    --paper: #ffffff;
    --ink: #1a1a1a;
    --muted: #555555;
    --purple: #5b0a8c;
  }
  * { box-sizing: border-box; margin: 0; padding: 0; }
  html, body {
    width: 1200px; height: 1000px; overflow: hidden;
    background: var(--stage);
    font-family: "Open Sans", Arial, sans-serif;
  }
  .stage {
    width: 1200px; height: 1000px;
    display: flex; flex-direction: column; align-items: center; justify-content: center;
    gap: 40px;
  }
  .card {
    width: 760px; height: 434px;
    background: var(--paper);
    position: relative;
    overflow: hidden;
  }
  /* back */
  .card-back {
    display: flex; flex-direction: column; align-items: center; justify-content: center;
  }
  .back-mark {
    width: 120px; height: 120px; border-radius: 50%;
    background: var(--purple);
    margin-bottom: 22px;
  }
  .back-name {
    font-weight: 800; font-size: 44px; color: var(--ink); line-height: 1;
  }
  .back-web {
    margin-top: 14px;
    font-size: 18px; letter-spacing: 6px; color: var(--muted);
  }
  /* front */
  .front-mark {
    position: absolute; left: -40px; top: 30px;
    width: 380px; height: 380px; border-radius: 50%;
    background: var(--purple);
  }
  .front-name {
    position: absolute; right: 40px; top: 52px;
    font-weight: 800; font-size: 60px; color: var(--ink); line-height: 1;
  }
  .contact {
    position: absolute; right: 40px; top: 168px;
    text-align: right; color: var(--ink);
  }
  .person {
    font-weight: 600; font-size: 24px; color: var(--purple); line-height: 1.05;
  }
  .role {
    font-size: 17px; letter-spacing: 0.5px; margin-bottom: 6px;
  }
  .address { font-size: 17px; line-height: 1.25; margin-bottom: 4px; }
  .lines { list-style: none; }
  .lines li {
    font-size: 18px; line-height: 1.3;
    display: flex; justify-content: flex-end; align-items: center; gap: 10px;
  }
  .lines .text { color: var(--ink); }
  .lines .email, .lines .web { color: var(--muted); }
  .icon { width: 16px; height: 16px; flex: none; fill: var(--purple); }
</style>
</head>
<body>
<main class="stage">
  <section class="card card-back">
    <div class="back-mark"></div>
    <div class="back-name">Quolvex</div>
    <div class="back-web">www.quolvex.com</div>
  </section>

  <section class="card card-front">
    <div class="front-mark"></div>
    <div class="front-name">Quolvex</div>
    <div class="contact">
      <div class="person">MARA LINT</div>
      <div class="role">PRESIDENT</div>
      <div class="address">412 Harrow Lane<br>Elm Ridge, NY 10987</div>
      <ul class="lines">
        <li><span class="text">555 0142 7781</span>
          <svg class="icon" viewBox="0 0 16 16"><path d="M2 5c0-2 2-3 6-3s6 1 6 3l-3 1-1-2H6L5 6 2 5zM4 7h8l1 7H3l1-7zm4 2a2 2 0 100 4 2 2 0 000-4z"/></svg></li>
        <li><span class="text">555 0198 3364</span>
          <svg class="icon" viewBox="0 0 16 16"><path d="M4 1h8v14H4V1zm1.5 2v9h5V3h-5zM8 12.6a.8.8 0 100 1.6.8.8 0 000-1.6z"/></svg></li>
        <li><span class="text">555 0176 2259</span>
          <svg class="icon" viewBox="0 0 16 16"><path d="M4 1h6l2 2v3h2v8H2V6h2V1zm1.5 1.5v4h5v-3L9.5 2.5h-4zM4 9v2h8V9H4z"/></svg></li>
        <li><span class="text email">mara@quolvex.com</span>
          <svg class="icon" viewBox="0 0 16 16"><path d="M1 3h14v10H1V3zm1.5 1.5L8 9l5.5-4.5h-11z"/></svg></li>
        <li><span class="text web">www.quolvex.com</span>
          <svg class="icon" viewBox="0 0 16 16"><circle cx="8" cy="8" r="7"/><path d="M1 8h14M8 1c3 3 3 11 0 14M8 1c-3 3-3 11 0 14" stroke="#fff" stroke-width="1" fill="none"/></svg></li>
      </ul>
    </div>
  </section>
</main>
</body>
</html>
```